Penny Harvest

Logo and general packaging design for premium quality, price conscious super foods.

Initial product portfolio includes:

Organic Raw Chia Seeds - Resealable plastic bags with 3 x 5 label.
Organic Cold Pressed Coconut Oil (plastic jar) - 2.5 x 6.5 label

The design should be transferable to additional products.

Project requirements:

The design should be simple and the core trade dress should be no more than 2 or 3 colors. The logo should reproduce well in black/1 color.

The idea of this design is to convey quality and simplicity, like a "no frills", premium quality brand.

Deliverable: fully editable (text and illustration):

Logo.

Basic Jar label design.

Basic Bag label design.

Target Market(s)

Educated women aged 22-45

Industry/Entity Type

Plastic

Requirements
Must have
• Clear, simple logo, delivered in vector form, 1 color/black.
• Use of logo on 1 jar label and 1 bag label, each with product name and space for required and optional marketing content.
Nice to have
• Additional iterations of the design to demonstrate your concept of how we will visually vary additional items in jars and bags.
• i.e. What an additional product in a bag would look like for purposes of brand consistency and product differentiation on shelf or online in e-store.
Should not have
• overly detailed graphics that don't scale well and/or may be hard to read or understand. 4 color design elements (except to simiulate how the product may look through the clear jar or bag or how the product may be placed in a simulated surrounding or ad.

```html
<!DOCTYPE html>
<html lang="en">
<head>
<meta charset="utf-8">
<title>Penny Harvest – Raw Chia Seeds Bag Label</title>
<link rel="stylesheet" href="https://fonts.googleapis.com/css2?family=Sniglet:wght@400;800&family=Cinzel:wght@400&family=Open+Sans:wght@400&display=swap">
<style>
  :root {
    --page-bg: #ffffff;
    --caption-grey: #8a8a8a;
    --label-brown: #2f1810;
    --back-kraft: #c4b5a0;
    --leaf-green: #86c455;
    --logo-white: #ffffff;
    --seed-dark: #5a3a28;
    --seed-mid: #8c6a52;
    --ornament-tan: #b8a48a;
  }
  * { margin: 0; padding: 0; box-sizing: border-box; }
  html, body {
    width: 1200px;
    height: 996px;
    overflow: hidden;
    background: var(--page-bg);
  }
  .sheet {
    position: relative;
    width: 1200px;
    height: 996px;
  }
  .panel-caption {
    position: absolute;
    top: 28px;
    width: 520px;
    text-align: center;
    font-family: "Open Sans", Arial, sans-serif;
    font-size: 26px;
    color: var(--caption-grey);
    letter-spacing: 0.5px;
  }
  .panel-caption--front { left: 67px; }
  .panel-caption--back { left: 640px; }

  .label { position: absolute; }
  .label--front {
    left: 67px;
    top: 104px;
    width: 519px;
    height: 864px;
    background: var(--label-brown);
  }
  .label--back {
    left: 642px;
    top: 102px;
    width: 515px;
    height: 864px;
    background: var(--back-kraft);
  }

  .brand-name {
    position: absolute;
    left: 0;
    top: 92px;
    width: 100%;
    text-align: center;
    font-family: "Sniglet", "Comic Sans MS", sans-serif;
    font-weight: 400;
    color: var(--logo-white);
    font-size: 76px;
    line-height: 84px;
  }

  .hero-photo {
    position: absolute;
    left: 97px;
    top: 384px;
    width: 346px;
    height: 232px;
    border-radius: 50% 50% 50% 50% / 60% 60% 40% 40%;
    background: linear-gradient(120deg, var(--leaf-green) 0%, var(--leaf-green) 22%, var(--seed-mid) 45%, var(--seed-dark) 100%);
    opacity: 0.9;
  }

  .product-claim {
    position: absolute;
    left: 0;
    top: 686px;
    width: 100%;
    text-align: center;
    font-family: "Sniglet", "Comic Sans MS", sans-serif;
    font-weight: 800;
    font-size: 30px;
    line-height: 36px;
    color: var(--leaf-green);
  }
  .divider-flourish {
    position: absolute;
    left: 191px;
    top: 738px;
    width: 158px;
    height: 26px;
    border-radius: 13px;
    background: linear-gradient(90deg, rgba(184,164,138,0) 0%, var(--ornament-tan) 30%, var(--ornament-tan) 70%, rgba(184,164,138,0) 100%);
    opacity: 0.75;
  }
  .product-name {
    position: absolute;
    left: 0;
    top: 776px;
    width: 100%;
    text-align: center;
    font-family: "Cinzel", Georgia, serif;
    font-size: 30px;
    color: var(--logo-white);
    letter-spacing: 1.5px;
  }
</style>
</head>
<body>
  <main class="sheet">
    <div class="panel-caption panel-caption--front">FRONT LABEL</div>
    <div class="panel-caption panel-caption--back">BACK LABEL</div>

    <section class="label label--front">
      <h1 class="brand-name">Penny<br>Harvest</h1>

      <div class="hero-photo" role="img" aria-label="Green leaf beside a leaf-shaped close-up photograph of raw chia seeds"></div>

      <div class="product-claim">ORGANIC</div>
      <div class="divider-flourish" role="img" aria-label="Decorative scroll flourish"></div>
      <div class="product-name">RAW CHIA SEEDS</div>
    </section>

    <section class="label label--back"></section>
  </main>
</body>
</html>
```